Crest of Morning Paddocks Business Cards with logo

Need a creative business card that pops. Colorful but professional. The attached logo should be included. We are a national horse racing partnership so we are in the equine business. Nothing cartoonlike or whimsical.

Target Market(s)

professionals - 40+

Contact Information for Business Card

Maren Dunleavy
Director of Operations
27 Ashbrook Lane
Middletown, MD. 21584

Phone (313) 555-0147

FX: (949) 555-0192

email: maren@cmpaddocks.example
cmpaddocks.example

Requirements
Must have
• All information above should be on the business card including the website address. Professional yet creative
Nice to have
• an attention grabbing design. not boring. exciting.
Should not have
• cartoon like - whimsical.

```html
<!DOCTYPE html>
<html lang="en">
<head>
<meta charset="utf-8">
<title>Crest of Morning Paddocks — Business Card</title>
<link rel="stylesheet" href="https://fonts.googleapis.com/css2?family=Jost:wght@300;400;500&display=swap">
<style>
  :root {
    --navy: #2b3272;
    --gold: #c29b3b;
    --photo-light: #e9c764;
    --photo-mid: #a8863a;
    --photo-dark: #3f3120;
    --card: #ffffff;
    --backdrop: #e8e5e0;
    --text: #2b3272;
  }
  html, body {
    margin: 0;
    width: 1200px;
    height: 1200px;
    overflow: hidden;
    background: var(--backdrop);
    font-family: "Jost", "Futura", sans-serif;
  }
  .business-card {
    position: absolute;
    left: 100px;
    top: 287px;
    width: 1000px;
    height: 626px;
    background: var(--card);
    box-shadow: 0 6px 18px rgba(0,0,0,0.18);
    overflow: hidden;
  }
  .card-art {
    position: absolute;
    inset: 0;
    width: 100%;
    height: 100%;
  }
  .website-band {
    position: absolute;
    left: 34px;
    top: 527px;
    height: 58px;
    line-height: 58px;
    font-size: 30px;
    font-weight: 400;
    color: #ffffff;
    letter-spacing: 0.5px;
  }
  .brand-mark {
    position: absolute;
    left: 700px;
    top: 40px;
    width: 280px;
    display: flex;
    flex-direction: column;
    align-items: center;
    gap: 14px;
  }
  .brand-dot {
    width: 76px;
    height: 76px;
    border-radius: 50%;
    background: var(--gold);
  }
  .brand-name {
    font-size: 22px;
    font-weight: 500;
    color: var(--navy);
    text-transform: uppercase;
    letter-spacing: 3px;
    text-align: center;
    line-height: 1.35;
  }
  .contact-block {
    position: absolute;
    right: 42px;
    top: 262px;
    text-align: right;
    color: var(--text);
  }
  .person-name {
    font-size: 38px;
    font-weight: 400;
    margin: 0;
    line-height: 1.15;
  }
  .person-title {
    font-size: 28px;
    font-weight: 500;
    margin: 2px 0 0;
    line-height: 1.3;
  }
  .address, .contact-lines {
    font-size: 26px;
    font-weight: 300;
    line-height: 1.45;
    margin: 0;
  }
  .contact-lines { margin-top: 34px; }
  .label { font-weight: 500; }
</style>
</head>
<body>
  <div class="business-card">
    <svg class="card-art" viewBox="0 0 658 412" preserveAspectRatio="none" aria-hidden="false">
      <defs>
        <linearGradient id="photoTone" x1="0" y1="0" x2="1" y2="1">
          <stop offset="0" stop-color="var(--photo-light)"/>
          <stop offset="0.45" stop-color="var(--photo-mid)"/>
          <stop offset="1" stop-color="var(--photo-dark)"/>
        </linearGradient>
      </defs>
      <polygon class="photo-area" role="img" aria-label="Photograph of a jockey riding a racehorse at full gallop, toned in gold" points="0,0 380,0 276,412 0,412" fill="url(#photoTone)"/>
      <polygon class="website-band-bg" points="0,347 292,347 283,385 0,385" fill="var(--navy)"/>
      <polygon class="stripe stripe-navy" points="384,0 392,0 288,412 280,412" fill="var(--navy)"/>
      <polygon class="stripe stripe-gold" points="399,0 416,0 312,412 295,412" fill="var(--gold)"/>
      <polygon class="stripe stripe-navy" points="424,0 432,0 328,412 320,412" fill="var(--navy)"/>
    </svg>

    <div class="website-band">www.cmpaddocks.example</div>

    <div class="brand-mark">
      <div class="brand-dot"></div>
      <div class="brand-name">Crest of Morning<br>Paddocks</div>
    </div>

    <div class="contact-block">
      <p class="person-name">Maren Dunleavy</p>
      <p class="person-title">Director of Operations</p>
      <p class="address">27 Ashbrook Lane<br>Middletown, MD. 21584</p>
      <p class="contact-lines">
        <span class="label">Phone:</span> (313) 555-0147<br>
        <span class="label">FX:</span> (949) 555-0192<br>
        <span class="label">Email:</span> maren@cmpaddocks.example
      </p>
    </div>
  </div>
</body>
</html>
```